Copper lark buildworks

Copper lark buildworks is a small construction company.
Who is a licenced builder, Carpenter, joiner,
working on heritage ,new build, speacial projects and sometimes furniture

Industry/Entity Type

Construction

```html
<!DOCTYPE html>
<html lang="en">
<head>
<meta charset="utf-8">
<title>Copper lark buildworks – business card</title>
<link rel="stylesheet" href="https://fonts.googleapis.com/css2?family=Montserrat:wght@300;400;600;700;800&display=swap">
<style>
  :root {
    --bg: #e7e6e3;
    --card-dark: #0c0c0c;
    --card-mid: #1c1c1c;
    --brand-green: #4cb81c;
    --band-green: #3e7f0c;
    --silver-light: #f2f2f2;
    --silver-dark: #9a9a9a;
    --text-light: #ffffff;
    --text-dark: #1a1a1a;
  }
  * { box-sizing: border-box; margin: 0; padding: 0; }
  html, body {
    width: 1200px; height: 1000px; overflow: hidden;
    background: var(--bg);
    font-family: "Montserrat", Arial, sans-serif;
  }
  .card {
    position: absolute; left: 150px; top: 243px;
    width: 900px; height: 514px;
    border-radius: 30px; overflow: hidden;
    background: radial-gradient(ellipse at 75% 20%, var(--card-mid), var(--card-dark) 70%);
    box-shadow: 0 10px 30px rgba(0,0,0,.25);
  }
  .card__swoosh { position: absolute; inset: 0; width: 900px; height: 514px; }
  .brand {
    position: absolute; right: 44px; top: 44px;
    text-align: right;
    color: var(--brand-green);
    font-weight: 800; font-size: 44px; line-height: 1;
    text-transform: uppercase; letter-spacing: -1px;
  }
  .contact {
    position: absolute; right: 44px; top: 150px;
    text-align: right; color: var(--text-light);
  }
  .contact__name { color: var(--brand-green); font-weight: 700; font-size: 25px; }
  .contact__role { font-size: 17px; font-weight: 400; margin-top: 2px; }
  .contact__lines { list-style: none; margin-top: 26px; font-size: 20px; line-height: 30px; }
  .contact__lines li { display: flex; justify-content: flex-end; align-items: center; gap: 10px; }
  .contact__lines li.no-icon { padding-right: 30px; }
  .icon { width: 20px; height: 20px; flex: none; }
  .services {
    position: absolute; left: 48px; bottom: 44px;
    list-style: none; font-size: 22px; line-height: 27px;
    color: var(--text-light); font-weight: 600;
  }
  .services__intro { color: var(--text-dark); font-weight: 400; }
</style>
</head>
<body>
  <article class="card">
    <svg class="card__swoosh" viewBox="0 0 900 514" aria-hidden="true">
      <defs>
        <linearGradient id="silver" x1="0" y1="0" x2="1" y2="1">
          <stop offset="0" stop-color="var(--silver-light)"/>
          <stop offset="1" stop-color="var(--silver-dark)"/>
        </linearGradient>
      </defs>
      <path d="M0,196 Q250,400 680,514 L0,514 Z" fill="url(#silver)"/>
      <path d="M0,222 Q240,420 640,514 L0,514 Z" fill="var(--band-green)"/>
    </svg>

    <h1 class="brand">Copper lark<br>buildworks</h1>

    <section class="contact">
      <p class="contact__name">Owen Hartley</p>
      <p class="contact__role">Licenced Builder &amp; Carpenter</p>
      <ul class="contact__lines">
        <li class="no-icon">Your Street Address Here</li>
        <li class="no-icon">Riverton 40213</li>
        <li>0431927564
          <svg class="icon" viewBox="0 0 20 20"><circle cx="10" cy="10" r="10" fill="var(--brand-green)"/><path d="M6 5.5c1-.6 1.6.2 2 1.2.3.7-.3 1.2-.6 1.5.5 1.3 1.5 2.3 2.6 2.8.3-.4.8-.9 1.5-.6 1 .4 1.8 1 1.2 2-1.6 2.2-5 .3-6.6-2.2C5 8.3 4.7 6.4 6 5.5z" fill="#0c0c0c"/></svg>
        </li>
        <li>owen@copperlark.com
          <svg class="icon" viewBox="0 0 20 20"><circle cx="10" cy="10" r="10" fill="var(--brand-green)"/><rect x="5" y="6.5" width="10" height="7" fill="none" stroke="#0c0c0c" stroke-width="1.4"/><path d="M5 6.5l5 4 5-4" fill="none" stroke="#0c0c0c" stroke-width="1.4"/></svg>
        </li>
        <li>www.copperlark.com
          <svg class="icon" viewBox="0 0 20 20"><circle cx="10" cy="10" r="10" fill="var(--brand-green)"/><circle cx="10" cy="10" r="5.5" fill="none" stroke="#0c0c0c" stroke-width="1.3"/><ellipse cx="10" cy="10" rx="2.3" ry="5.5" fill="none" stroke="#0c0c0c" stroke-width="1.2"/><path d="M4.5 10h11" stroke="#0c0c0c" stroke-width="1.2"/></svg>
        </li>
      </ul>
    </section>

    <ul class="services">
      <li class="services__intro">working on</li>
      <li>heritage</li>
      <li>new build</li>
      <li>speacial projects</li>
      <li>and furniture</li>
    </ul>
  </article>
</body>
</html>
```